New labels for new line of supplements

I'm starting a new line of supplements and I need a label created for the first supplement - Glyco Steady Aid.
The supplement line is by Corvane Nutrition. What I'm really looking for is label that can be used again for the next supplement and consumers would recognize the label layout as a Corvane Nutrition product. I've attached an example from Pelminth Nutrition to have a look at. I've also attached my "Corvane Skin Care" logo that needs to be turned into Corvane Nutrition. Just change Skin Care to Nutrition.
Target Market(s)
Trelvix consumers
Colors
Designer to choose colors to be used in the design.
Requirements
Must have
- Instantly recognizable as my brand

```html
<!DOCTYPE html>
<html lang="en">
<head>
<meta charset="utf-8">
<title>Corvane Nutrition – Glyco Steady Aid Label</title>
<link href="https://fonts.googleapis.com/css2?family=Open+Sans:ital,wght@0,400;0,600;0,700;0,800;1,400&family=Roboto:ital,wght@1,400&family=Quicksand:wght@500&family=Share+Tech&display=swap" rel="stylesheet">
<style>
  :root {
    --lime: #c8e04e;
    --black: #1f1f1f;
    --navy: #0c3a6b;
    --blue: #1f7fc4;
    --sky: #35b4ee;
    --brand: #1b4f9c;
    --grey: #c4c4c4;
    --cream: #eef3cc;
    --white: #ffffff;
    --ink: #000000;
  }
  * { box-sizing: border-box; margin: 0; padding: 0; }
  html, body { width: 1200px; height: 1000px; overflow: hidden; background: var(--white); }
  .canvas { position: relative; width: 1200px; height: 1000px; font-family: "Open Sans", Arial, sans-serif; }
  .label-art { position: absolute; left: 0; top: 0; }

  .usage {
    position: absolute; left: 73px; top: 309px; width: 256px;
    color: var(--white); font-size: 11.4px; line-height: 15.2px;
  }
  .usage p { margin-bottom: 14px; }
  .usage strong { font-weight: 700; }
  .usage .warning { font-weight: 700; margin-bottom: 8px; }
  .fda-note {
    border: 1.5px solid var(--white); padding: 2px 4px;
    font-size: 9.6px; line-height: 11px; width: 248px; margin-left: -2px;
  }
  .lot { font-size: 10px; line-height: 12px; margin-top: 9px; }
  .lot .code { display: block; padding-left: 110px; }

  .claims {
    position: absolute; left: 358px; top: 307px; list-style: none;
    font-family: "Roboto", Arial, sans-serif; font-style: italic;
    color: var(--white); font-size: 18.5px; line-height: 30px;
  }
  .claims li::before { content: "• "; font-style: normal; }

  .brand-name {
    position: absolute; left: 442px; top: 505px; width: 255px; text-align: center;
    font-family: "Quicksand", Arial, sans-serif; font-weight: 500; color: var(--brand);
  }
  .brand-name .word { display: block; font-size: 42px; letter-spacing: 2px; line-height: 50px; }
  .brand-name .line { display: block; font-size: 15px; letter-spacing: 11px; line-height: 22px; padding-left: 11px; }

  .tag {
    position: absolute; color: var(--white);
    font-family: "Share Tech", monospace, sans-serif; letter-spacing: 1.5px;
    background: linear-gradient(90deg, var(--blue), var(--sky));
  }
  .tag.type { left: 474px; top: 622px; width: 184px; height: 20px; font-size: 12px; line-height: 20px; padding-left: 8px; transform: skewY(-1.5deg); }
  .tag.count { left: 474px; top: 655px; width: 186px; height: 24px; font-size: 14px; line-height: 24px; padding-left: 44px; letter-spacing: 2.5px; transform: skewY(1deg); }

  .facts {
    position: absolute; left: 788px; top: 310px; width: 255px; height: 403px;
    background: var(--white); border: 2.5px solid var(--ink); padding: 2px 5px; color: var(--ink);
  }
  .facts h2 { font-size: 22px; font-weight: 800; text-align: center; line-height: 28px; letter-spacing: -0.3px; }
  .facts .serving { font-size: 8.6px; font-weight: 700; border-bottom: 6px solid var(--ink); padding-bottom: 2px; text-align: center; }
  .facts table { width: 100%; border-collapse: collapse; font-size: 9.4px; }
  .facts th { font-weight: 700; font-size: 9.6px; text-align: right; padding: 3px 0; border-bottom: 3px solid var(--ink); }
  .facts td { border-bottom: 1px solid var(--ink); padding: 1px 0; line-height: 11.5px; vertical-align: top; }
  .facts td.name { font-weight: 700; }
  .facts td.name small { font-weight: 400; font-size: 7.2px; }
  .facts td.name .sub { display: block; font-weight: 400; font-size: 7.2px; padding-left: 18px; line-height: 9px; }
  .facts td.amt { text-align: right; padding-right: 6px; white-space: nowrap; }
  .facts td.dv { text-align: right; width: 28px; }
  .facts tr:last-child td { border-bottom: 3px solid var(--ink); }
  .facts .footnote { font-size: 9px; padding-top: 1px; }

  .inactive {
    position: absolute; left: 1048px; top: 709px; width: 290px; transform-origin: 0 0; transform: rotate(-90deg);
    font-size: 8.4px; color: var(--ink); white-space: nowrap;
  }
  .inactive strong { font-weight: 700; }
  .distributor {
    position: absolute; left: 1080px; top: 610px; width: 240px; transform-origin: 0 0; transform: rotate(-90deg);
    color: var(--white); font-size: 15.5px; line-height: 17px; text-align: center;
  }
</style>
</head>
<body>
<div class="canvas">
  <svg class="label-art" width="1200" height="1000" viewBox="0 0 1200 1000" aria-hidden="true">
    <defs>
      <linearGradient id="bannerFill" x1="0" y1="0" x2="1" y2="1">
        <stop offset="0" stop-color="#0c3a6b"/><stop offset="0.55" stop-color="#1f7fc4"/><stop offset="1" stop-color="#35b4ee"/>
      </linearGradient>
      <linearGradient id="stripFill" x1="0" y1="0" x2="0" y2="1">
        <stop offset="0" stop-color="#0c3a6b"/><stop offset="1" stop-color="#35b4ee"/>
      </linearGradient>
    </defs>
    <rect x="55" y="273" width="1088" height="25" fill="var(--lime)"/>
    <rect x="55" y="298" width="287" height="429" fill="var(--black)"/>
    <polygon points="55,727 150,680 250,727" fill="var(--grey)"/>
    <polygon points="170,727 342,620 342,727" fill="var(--lime)"/>
    <polygon points="170,727 240,690 290,727" fill="var(--cream)"/>
    <polygon points="342,298 693,298 580,403 342,403" fill="url(#bannerFill)"/>
    <polygon points="342,450 410,727 342,727" fill="url(#stripFill)"/>
    <polygon points="735,298 780,298 780,600" fill="url(#stripFill)"/>
    <polygon points="725,727 780,470 790,470 790,727" fill="var(--lime)"/>
    <rect x="780" y="298" width="285" height="429" fill="var(--lime)"/>
    <rect x="1065" y="298" width="78" height="429" fill="var(--black)"/>
  </svg>

  <section class="usage">
    <p><strong>Suggested Use:</strong> As a dietary supplement take one (1) veggie capsule twice a day. For best results take 20-30 min before a meal with an 8oz. glass of water or as directed by your healthcare professional.</p>
    <p><strong>CAUTION:</strong> Do not exceed recommended dose. Pregnant or nursing mothers, children under the age of 18, and individuals with a known medical condition should consult a physician before using this or any dietary supplement.</p>
    <p class="warning">KEEP OUT OF REACH OF CHILDREN.<br>DO NOT USE IF SAFETY SEAL IS DAMAGED OR MISSING. STORE IN A COOL, DRY PLACE.</p>
    <div class="fda-note">* These statements have not been evaluated by the Food and Drug Administration. This product is not intended to diagnose, treat, cure or prevent any disease.</div>
    <div class="lot">Lot # and Expiration Date Printed<br>on bottom of Bottle<span class="code">V4R0</span></div>
  </section>

  <ul class="claims">
    <li>Supports Healthy Blood Sugar*</li>
    <li>Immune Function Support*</li>
    <li>Plus Much More!*</li>
  </ul>

  <div class="brand-name"><span class="word">CORVANE</span><span class="line">NUTRITION</span></div>

  <div class="tag type">NUTRITION SUPPLEMENT</div>
  <div class="tag count">60 Capsules</div>

  <section class="facts">
    <h2>Supplement Facts</h2>
    <div class="serving">Serving Size: 1 Capsule &nbsp;Servings Per Container: 60</div>
    <table>
      <tr><th colspan="2">Amount Per Serving</th><th>%DV</th></tr>
      <tr><td class="name">Vitamin C <small>(ascorbic acid)</small></td><td class="amt">50 mg</td><td class="dv">83%</td></tr>
      <tr><td class="name">Vitamin E <small>(d-Alpha tocopheryl succinate)</small></td><td class="amt">15 IU</td><td class="dv">50%</td></tr>
      <tr><td class="name">Biotin</td><td class="amt">300 mcg</td><td class="dv">100%</td></tr>
      <tr><td class="name">Magnesium <small>(oxide)</small></td><td class="amt">125 mg</td><td class="dv">31%</td></tr>
      <tr><td class="name">Zinc <small>(oxide)</small></td><td class="amt">7.5 mg</td><td class="dv">50%</td></tr>
      <tr><td class="name">Manganese <small>(as amino acid chelate)</small></td><td class="amt">1 mg</td><td class="dv">50%</td></tr>
      <tr><td class="name">Chromium <small>(as amino acid chelate)</small></td><td class="amt">67 mcg</td><td class="dv">56%</td></tr>
      <tr><td class="name">Banaba Leaf <small>(1% extract)</small><span class="sub">(Lagerstroemia Speciosa)</span></td><td class="amt">25 mg</td><td class="dv">**</td></tr>
      <tr><td class="name">Guggul <small>(10% extract)(resin)</small></td><td class="amt">50 mg</td><td class="dv">**</td></tr>
      <tr><td class="name">Bitter Melon <small>(4:1 extract)(fruit)</small></td><td class="amt">50 mg</td><td class="dv">**</td></tr>
      <tr><td class="name">Licorice Root Extract</td><td class="amt">50 mg</td><td class="dv">**</td></tr>
      <tr><td class="name">Cinnamon Bark Powder<span class="sub">(cinnamomum cassia)</span></td><td class="amt">50 mg</td><td class="dv">**</td></tr>
      <tr><td class="name">Gymnema Sylvestre Leaf Powder</td><td class="amt">50 mg</td><td class="dv">**</td></tr>
      <tr><td class="name">Yarrow Flowers Powder</td><td class="amt">25 mg</td><td class="dv">**</td></tr>
      <tr><td class="name">Cayenne Pepper Powder<span class="sub">(40M HU/G)(fruit)</span></td><td class="amt">10 mg</td><td class="dv">**</td></tr>
      <tr><td class="name">Juniper Berry Powder</td><td class="amt">25 mg</td><td class="dv">**</td></tr>
      <tr><td class="name">White Mulberry Leaf Powder</td><td class="amt">25 mg</td><td class="dv">**</td></tr>
      <tr><td class="name">Vanadium <small>(vanadyl sulfate)</small></td><td class="amt">200 mcg</td><td class="dv">**</td></tr>
      <tr><td class="name">Alpha Lipoic Acid</td><td class="amt">30 mg</td><td class="dv">**</td></tr>
      <tr><td class="name">L-Taurine</td><td class="amt">25 mg</td><td class="dv">**</td></tr>
    </table>
    <div class="footnote">** Daily Value (DV) not established</div>
  </section>

  <div class="inactive"><strong>Inactive Ingredients:</strong> Cellulose (Vegetable Capsule), Rice Bran.</div>
  <div class="distributor">Distributed By: Company Name<br>Addres, City, State zipcode<br>Website or Phone number</div>
</div>
</body>
</html>
```